'Ormel Property Development' Business Card

Business Card Features:

High Quality (potentially textured) thick card - preference is white textured card

Logo (supplied)

We plan to use the vertical logo as the main logo. But i am happy for people to use either if they find it works better for the design of the card.

The building icon and also the insert to the 'E' is in a metallic finish, i think this should be finished in a metallic embossed or raised style.
Updates

Please note i have attached both a horizontal and Vertical Logo for your reference. We plan to use the vertical logo as the main logo. But i am happy for people to use either if they find it works better for the design of the card.

Please note i am considering having the cards made on stainless steel. This introduces the option of having cut outs in the card and etching or printing for the design. If you have a good concept for this please submit.

http://www.tinquarry.example/black-metal-cards# this is a site that makes the metal cards to offer some direction . . . . Please note i am basic the selection o the best design, if that means normal print cards on paper then this is what i will choose. But there are some great options with the metal. Thanks.

Industry/Entity Type

Building

Requirements
Must have
• Helvetica font to details side of card - logo as supplied to opposite side.

Card Details:

Darrow Pketts
Managing Director

+61 487 263 518
+61 3 6172 4809

PO Box 73
Bentleigh, VIC 3024

darrow@ormel.example

www.ormel.example

```html
<!DOCTYPE html>
<html lang="en">
<head>
<meta charset="utf-8">
<title>Ormel Property Development — Business Card</title>
<link rel="stylesheet" href="https://fonts.googleapis.com/css2?family=Arimo:wght@400;700&display=swap">
<style>
  :root {
    --backdrop: #e4e4e4;
    --paper: #fbfbfb;
    --band-dark: #4a4e51;
    --band-light: #62666a;
    --rule: #9a9da0;
    --ink-name: #3f4346;
    --ink-soft: #7a7d80;
    --ink-brand: #6c6f72;
    --ink-band: #a7abae;
    --ink-reverse: #f2f2f2;
  }
  * { margin: 0; padding: 0; box-sizing: border-box; }
  html, body {
    width: 1200px; height: 720px; overflow: hidden;
    background: var(--backdrop);
    font-family: "Helvetica Neue", Helvetica, Arimo, Arial, sans-serif;
  }
  .canvas { position: relative; width: 1200px; height: 720px; }

  .card {
    position: absolute; top: 242px;
    width: 420px; height: 240px; overflow: hidden;
  }
  .card--front { left: 147px; background: var(--paper); }
  .card--back {
    left: 633px;
    background: linear-gradient(120deg, var(--band-light), var(--band-dark));
    display: flex; align-items: center; justify-content: center;
  }

  .brand {
    position: absolute; left: 18px; top: 16px;
    display: flex; align-items: center; gap: 12px;
  }
  .brand__mark { width: 40px; height: 40px; background: var(--ink-brand); }
  .brand__name {
    color: var(--ink-brand); font-weight: 700; font-size: 15px;
    line-height: 1.2; width: 140px;
  }

  .person { position: absolute; left: 18px; top: 103px; }
  .person__name { color: var(--ink-name); font-weight: 700; font-size: 13px; }
  .person__role { color: var(--ink-soft); font-size: 10px; margin-top: 2px; }

  .details-band {
    position: absolute; left: 0; right: 0; top: 148px; bottom: 0;
    background: linear-gradient(120deg, var(--band-light), var(--band-dark));
    border-top: 2px solid var(--rule);
  }
  .contacts { position: absolute; left: 18px; top: 24px; list-style: none; }
  .contacts li {
    display: flex; align-items: center; gap: 7px;
    color: var(--ink-band); font-size: 10px; line-height: 12px;
  }
  .contacts svg { width: 10px; height: 10px; fill: none; stroke: var(--ink-reverse); stroke-width: 1.3; }
  .address {
    position: absolute; left: 303px; top: 52px;
    color: var(--ink-band); font-size: 10px; line-height: 12px; font-style: normal;
  }

  .back-brand {
    color: var(--ink-reverse); font-weight: 700; font-size: 24px;
    text-align: center; line-height: 1.2;
  }
</style>
</head>
<body>
<main class="canvas">
  <section class="card card--front" aria-label="Card details side">
    <div class="brand">
      <span class="brand__mark"></span>
      <span class="brand__name">Ormel Property Development</span>
    </div>
    <div class="person">
      <p class="person__name">Darrow Pketts</p>
      <p class="person__role">Managing Director</p>
    </div>
    <div class="details-band">
      <ul class="contacts">
        <li><svg viewBox="0 0 10 10"><path d="M1 3 Q5 0 9 3 L8 4 L6.5 3.5 L3.5 3.5 L2 4 Z M2.5 5 H7.5 V9 H2.5 Z"/></svg>0487263518</li>
        <li><svg viewBox="0 0 10 10"><rect x="2.5" y="0.8" width="5" height="8.4" rx="0.8"/><path d="M4.5 7.8 H5.5"/></svg>1800 417 293</li>
        <li><svg viewBox="0 0 10 10"><rect x="0.8" y="2" width="8.4" height="6"/><path d="M0.8 2 L5 5.5 L9.2 2"/></svg>darrow@ormel.example</li>
        <li><svg viewBox="0 0 10 10"><rect x="0.8" y="1.2" width="8.4" height="5.8"/><path d="M3 9 H7 M5 7 V9"/></svg>www.ormel.example</li>
      </ul>
      <address class="address">PO BOX 73 Bentleigh,<br>VIC 3024</address>
    </div>
  </section>

  <section class="card card--back" aria-label="Card logo side">
    <p class="back-brand">Ormel<br>Property Development</p>
  </section>
</main>
</body>
</html>
```